LOGO DESIGN: Construction Related Service Business

We require a logo for our business Tovar Services. We are a construction related business offering a range of services including machine services for groundworks (digging trenches, soak wells, preparing land for construction etc), demolition and truck haulage from demolition sites.
We would like our logo to be predominately text, but may include abstract graphics. The colour scheme should be mainly a mid bright blue and overall be quite 'clean'.

Industry/Entity Type

Construction

Contact Information for Business Card

Dale Morrow
Ph:041 592 3068
tovarservices@quillnet.com.au

Colors
0456a3

```html
<!DOCTYPE html>
<html lang="en">
<head>
<meta charset="utf-8">
<title>Tovar Services — Business Card</title>
<link rel="stylesheet" href="https://fonts.googleapis.com/css2?family=Marcellus&family=Exo+2:wght@600&family=Questrial&family=Arimo&display=swap">
<style>
  :root {
    --page-bg: #6b6b6b;
    --card-white: #ffffff;
    --brand-blue: #0456a3;
    --band-top: #1f8ad6;
    --band-bottom: #0b3ea4;
    --muted-grey: #7a7a7a;
    --contact-white: #ffffff;
    --mark-blue: #1560c0;
    --deco-tint: rgba(140, 150, 230, 0.28);
  }
  * { margin: 0; padding: 0; box-sizing: border-box; }
  html, body {
    width: 1200px;
    height: 988px;
    overflow: hidden;
    background: var(--page-bg);
  }
  .card {
    position: absolute;
    left: 120px;
    top: 217px;
    width: 960px;
    height: 553px;
    background: var(--card-white);
    overflow: hidden;
    box-shadow: 0 6px 18px rgba(0, 0, 0, 0.25);
  }
  .brand {
    position: absolute;
    left: 41px;
    top: 40px;
  }
  .brand-dot {
    display: block;
    width: 118px;
    height: 118px;
    margin-left: 88px;
    border-radius: 50%;
    background: var(--mark-blue);
  }
  .brand-name {
    display: block;
    margin-top: 30px;
    font-family: "Marcellus", serif;
    font-size: 46px;
    line-height: 1;
    color: var(--brand-blue);
  }
  .holder {
    position: absolute;
    left: 621px;
    top: 30px;
  }
  .holder-name {
    font-family: "Exo 2", sans-serif;
    font-weight: 600;
    font-size: 46px;
    line-height: 1;
    color: var(--brand-blue);
  }
  .holder-role {
    margin-top: 10px;
    font-family: "Arimo", sans-serif;
    font-size: 27px;
    line-height: 1;
    color: var(--muted-grey);
  }
  .band {
    position: absolute;
    left: 0;
    top: 288px;
    width: 960px;
    height: 265px;
    background: linear-gradient(180deg, var(--band-top) 0%, var(--band-bottom) 100%);
  }
  .band-deco {
    position: absolute;
    right: -60px;
    top: 40px;
    width: 300px;
    height: 300px;
    border-radius: 50%;
    background: var(--deco-tint);
  }
  .contacts {
    position: absolute;
    left: 41px;
    top: 158px;
    list-style: none;
    font-family: "Questrial", sans-serif;
    font-size: 28px;
    line-height: 34px;
    color: var(--contact-white);
  }
  .contact-line {
    display: flex;
    align-items: center;
    gap: 10px;
  }
  .contact-icon {
    width: 22px;
    height: 22px;
    flex: none;
  }
</style>
</head>
<body>
  <main class="card">
    <div class="brand">
      <span class="brand-dot"></span>
      <span class="brand-name">Tovar Services</span>
    </div>

    <div class="holder">
      <p class="holder-name">Dale Morrow</p>
      <p class="holder-role">Owner</p>
    </div>

    <section class="band">
      <div class="band-deco"></div>
      <ul class="contacts">
        <li class="contact-line">
          <svg class="contact-icon" viewBox="0 0 24 24" aria-hidden="true">
            <path fill="#ffffff" d="M7 2c1 0 1.5.6 2 1.6l1.2 2.6c.4.9.2 1.6-.5 2.2l-1.3 1c.9 2.1 2.3 3.7 4.3 5l1.1-1.2c.6-.7 1.4-.8 2.2-.4l2.6 1.3c.9.5 1.3 1.1 1.1 2l-.5 2c-.3 1.1-1.2 1.8-2.4 1.7C9 19.2 3.9 13.5 4 5.6 4 4.4 4.7 3.4 5.8 3.1z"/>
          </svg>
          <span>041 592 3068</span>
        </li>
        <li class="contact-line">
          <svg class="contact-icon" viewBox="0 0 24 24" aria-hidden="true">
            <rect x="2.5" y="6" width="19" height="13" rx="1.5" fill="none" stroke="#ffffff" stroke-width="2"/>
            <path d="M3 7l9 7 9-7" fill="none" stroke="#ffffff" stroke-width="2"/>
          </svg>
          <span>tovarservices@quillnet.com.au</span>
        </li>
      </ul>
    </section>
  </main>
</body>
</html>
```